Business card and company logo design needed

Need a business card and company logo design for all stationary for an Aviation refueling consultancy business. Our business offers consulting services in the specialist aviation refueling industry. Services range from engineering, compliance and management consultancy through to project management services. This encompasses infrastructure from refinery through to airport and into the aircraft wing.

Design should be simple, 'less-is-more' concept, possibly taking advantage of the 'm' for tovel and the fact is it the aviation industry. It should convey confidence, safety, experience, professionalism, aviation, engineering?, and should not be afraid to be simple in color...though please do not let this restrict your designs and imagination.

Target Market(s)

Airport authorities, oil majors, aircraft operators

Industry/Entity Type

Airport

Contact Information for Business Card

Verlin Skyward Advisory Pty Ltd
Dario Tovel
Director
mobile:+61428537104
email: dario@tovelexample.com
Talkvexa: dario.tovelexample

Logo styles of interest
Emblem Logo
Pictorial/Combination Logo
Abstract Logo
Wordmark Logo
Lettermark Logo
Requirements
Must have
• - A feel of safety, security and confidence
Nice to have
• - Aviation has both heritage and modern 'sexy' elements so would be nice to try and capture both
- Aviation 'JET' fuel color is designated as black in signage or labels
- Themes? : Aviation fuel is derived from oil, it burns, safety, Jet fuel is colorless
- Company is global in reach, borderless like aircraft
Should not have
• - Cliche:

```html
<!DOCTYPE html>
<html lang="en">
<head>
<meta charset="utf-8">
<title>Verlin Skyward Advisory – Business Card</title>
<link rel="stylesheet" href="https://fonts.googleapis.com/css2?family=Open+Sans:wght@400&family=Montserrat:wght@700;800&display=swap">
<style>
  :root {
    --backdrop: #1d1b19;
    --card: #ffffff;
    --ink: #1a1a1a;
    --ink-soft: #4a4a4a;
    --accent-blue: #3d8fd6;
    --rule: #6a6a6a;
  }
  * { box-sizing: border-box; margin: 0; padding: 0; }
  html, body {
    width: 1200px;
    height: 1000px;
    overflow: hidden;
    background: var(--backdrop);
  }
  .stage {
    position: relative;
    width: 1200px;
    height: 1000px;
  }
  .card {
    position: absolute;
    top: 230px;
    width: 330px;
    height: 540px;
    background: var(--card);
    box-shadow: 0 12px 30px rgba(0,0,0,0.5);
  }
  .card--front { left: 225px; }
  .card--back  { left: 645px; }

  /* Front */
  .brand {
    position: absolute;
    top: 130px;
    left: 0;
    right: 0;
    display: flex;
    flex-direction: column;
    align-items: center;
  }
  .brand__dot {
    width: 100px;
    height: 100px;
    border-radius: 50%;
    background: var(--ink);
    margin-bottom: 22px;
  }
  .brand__name {
    font-family: "Open Sans", sans-serif;
    font-weight: 400;
    font-size: 24px;
    line-height: 1.15;
    color: var(--ink);
    text-align: center;
  }
  .brand__sub {
    font-family: "Open Sans", sans-serif;
    font-weight: 400;
    font-size: 17px;
    line-height: 1.2;
    color: var(--ink-soft);
    text-align: center;
  }

  /* Back */
  .role {
    position: absolute;
    top: 28px;
    left: 28px;
  }
  .role__title {
    font-family: "Montserrat", sans-serif;
    font-weight: 800;
    font-size: 16px;
    color: var(--ink);
    letter-spacing: -0.3px;
    border-bottom: 1.5px solid var(--rule);
    padding-bottom: 1px;
  }
  .role__name {
    font-family: "Open Sans", sans-serif;
    font-size: 15px;
    color: var(--ink-soft);
    white-space: nowrap;
  }
  .contact {
    position: absolute;
    left: 0;
    right: 0;
    top: 250px;
    text-align: center;
  }
  .contact__label {
    font-family: "Montserrat", sans-serif;
    font-weight: 800;
    font-size: 16px;
    color: var(--ink);
    line-height: 1.05;
    margin-top: 10px;
  }
  .contact__label--chat { color: var(--accent-blue); }
  .contact__value {
    font-family: "Open Sans", sans-serif;
    font-size: 17px;
    color: var(--ink);
    line-height: 1.2;
  }
</style>
</head>
<body>
<main class="stage">
  <section class="card card--front" aria-label="Business card front">
    <div class="brand">
      <span class="brand__dot"></span>
      <p class="brand__name">Verlin Skyward</p>
      <p class="brand__sub">Advisory Pty Ltd</p>
    </div>
  </section>

  <section class="card card--back" aria-label="Business card back">
    <div class="role">
      <p class="role__title">Director</p>
      <p class="role__name">Dario Tovel</p>
    </div>
    <div class="contact">
      <p class="contact__label">mobile</p>
      <p class="contact__value">+61428537104</p>
      <p class="contact__label">email</p>
      <p class="contact__value">dario@tovelexample.com</p>
      <p class="contact__label contact__label--chat">Talkvexa</p>
      <p class="contact__value">dario.tovelexample</p>
    </div>
  </section>
</main>
</body>
</html>
```